Home Page Design (+50 More Pages To Winning Designer!)

We have a 50+ page website, but we're starting with the home page. The winning designer will get all 50+ pages to design as a 2nd project, so make sure you do your best!

SoarVane is in the private jet industry and needs a re-designed website.

We have created the structure for the website and content inside of Tavoni.io (THESE ARE ONLY ROUGH A.I. GENERATED WIREFRAMES AND DO NOT NEED TO BE FOLLOWED EXACTLY) - https://www.tavoni.io/app/project/P482915_qRuVwKsLm-DDtaHrYuop72XNc8fkoPzqlrhwDxHkaWm3Tq

Take the content from the 'Home Page' under the 'Wireframe' tab on the Tavoni.io link above, but feel free to re-design the page in a better way as these are only A.I. generated wireframes.

We want a DARK theme.... High quality, luxurious feel, greyscale colors. Attached is a brand guideline (BUT THIS IS NOT A 100% BRAND GUIDELINE, YOU CAN CHANGE COLORS AND FONTS AND MAKE CHANGES IF YOU HAVE BETTER IDEAS) and attached is our logo. We are also attaching some examples of other apps and websites to give you a guideline of what we're looking for for this design project.

The final design MUST communicate luxury using high-quality imagery of large cabin luxurious private jets.

ENTRIES THAT DO NOT FOLLOW THE PROJECT BRIEF WILL BE AUTOMATICALLY DISCARDED. FOLLOW THE INSTRUCTIONS!

Industry/Entity Type

Travel

Number of Pages Required

1 page

Font styles to use
Sans Serif

Colors

Designer to choose colors to be used in the design.

Requirements
Must have
• Follow wireframe and use content in wireframe (see Tavoni.io link)

```html
<!DOCTYPE html>
<html lang="en">
<head>
<meta charset="utf-8">
<title>SoarVane — Private Jet Travel</title>
<link href="https://fonts.googleapis.com/css2?family=Plus+Jakarta+Sans:wght@400;500;600;700;800&display=swap" rel="stylesheet">
<style>
:root{
  --bg:#000;
  --header:#1a1a1a;
  --card:#161616;
  --text:#fff;
  --muted:#d6d6d6;
  --gold:#b8913f;
  --btn-text:#a8843a;
  --font:"Plus Jakarta Sans", Arial, sans-serif;
}
*{box-sizing:border-box;margin:0;padding:0}
html,body{width:1200px;height:3418px;overflow:hidden;background:var(--bg);color:var(--text);font-family:var(--font)}
.page{position:relative;width:1200px;height:3418px}

.site-header{position:absolute;left:0;top:0;width:1200px;height:60px;background:var(--header);z-index:2}
.brand{position:absolute;left:66px;top:17px;display:flex;align-items:center;gap:7px;font-size:19px;font-weight:500;letter-spacing:-.2px}
.brand-mark{width:10px;height:10px;background:var(--text)}

.photo{position:absolute}
.hero-photo{left:0;top:0;width:1200px;height:600px;background:linear-gradient(90deg,rgba(0,0,0,.6) 0%,rgba(0,0,0,.2) 55%,rgba(0,0,0,.05) 100%),linear-gradient(180deg,#6e5a48 0%,#9b8672 35%,#4c3e33 75%,#2c241d 100%)}
.band-photo{left:0;top:1700px;width:1200px;height:431px;background:linear-gradient(90deg,rgba(0,0,0,.55) 0%,rgba(0,0,0,.15) 60%,rgba(0,0,0,.1) 100%),linear-gradient(180deg,#8a7a68 0%,#a08a6e 40%,#5a4328 70%,#2f2418 100%)}
.side-photo{left:66px;width:524px;height:522px}
.host-photo{top:683px;background:linear-gradient(120deg,#e8ddd0 0%,#c9b49e 40%,#7a2a20 75%,#4a1712 100%)}
.business-photo{top:2216px;background:linear-gradient(120deg,#7a2822 0%,#dcd0bd 40%,#3a3230 70%,#2a1614 100%)}
.frame{position:absolute;left:84px;width:522px;height:521px;border:1px solid var(--gold);opacity:.8}

.eyebrow{position:absolute;display:flex;align-items:center;gap:9px;font-size:11px;font-weight:600;letter-spacing:5px;text-transform:uppercase;color:var(--gold)}
.eyebrow::before{content:"";display:block;width:83px;height:1px;background:var(--gold)}
.eyebrow.case{text-transform:none}
.eyebrow.bare::before{display:none}

.display{position:absolute;font-size:42px;font-weight:700;line-height:55px;letter-spacing:.9px}
.lede{position:absolute;font-size:13px;line-height:22.5px;color:var(--muted)}

.btn{position:absolute;height:39px;width:160px;display:flex;align-items:center;justify-content:center;font-size:13px;font-weight:600}
.btn-solid{background:#fff;color:var(--btn-text)}
.btn-line{border:1px solid #cfcfcf;color:#fff}
.btn.sm{width:149px}

.ticks{position:absolute;font-size:13.5px;font-weight:600}
.ticks span{position:absolute;white-space:nowrap}
.ticks span::before{content:"•";color:var(--gold);margin-right:5px}

.card{position:absolute;top:1306px;width:342px;height:309px;background:var(--card)}
.ring{position:absolute;width:51px;height:51px;border:1.3px solid var(--gold);border-radius:50%}
.card .ring{left:30px;top:36px}
.card h3,.service h3{position:absolute;font-size:27px;font-weight:700;line-height:36px;letter-spacing:.5px}
.card h3{left:30px;top:109px;width:300px}
.card p,.service p{position:absolute;font-size:12.5px;line-height:22.5px;color:var(--muted)}
.card p{left:29px;top:193px;width:285px}

.feature{position:absolute;width:220px}
.feature h4{font-size:16px;font-weight:700;line-height:22px}
.feature h4::before{content:"•";color:var(--gold);margin-right:5px;font-size:13px}
.feature p{font-size:12.5px;line-height:22.5px;color:var(--muted);margin-top:10px}

.service{position:absolute;top:3034px;width:300px;height:230px}
.service .ring{left:0;top:0}
.service h3{left:0;top:71px;width:260px;line-height:35px}
.service p{left:0;top:155px;width:280px}
</style>
</head>
<body>
<div class="page">

  <header class="site-header">
    <div class="brand"><span>SoarVane</span><span class="brand-mark"></span></div>
  </header>

  <section class="hero">
    <div class="photo hero-photo" role="img" aria-label="Wide private jet cabin with cream leather club seats, sofa and carpeted aisle"></div>
    <div class="eyebrow bare" style="left:158px;top:296px">Welcome</div>
    <h1 class="display" style="left:66px;top:320px;width:420px">Experience the ultimate in luxury travel jet</h1>
    <a class="btn btn-solid" style="left:66px;top:510px">Explore</a>
    <a class="btn btn-line" style="left:236px;top:510px">Learn More</a>
  </section>

  <section class="discover">
    <div class="frame" style="top:700px"></div>
    <div class="photo side-photo host-photo" role="img" aria-label="Flight attendant welcoming guests beside a cream leather jet seat"></div>
    <div class="eyebrow" style="left:656px;top:742px">Discover</div>
    <h2 class="display" style="left:656px;top:770px;width:490px">Experience the luxury of fractional jet ownership</h2>
    <p class="lede" style="left:656px;top:948px;width:480px">With SoarVane's fractional jet ownership program, you can enjoy the benefits of private jet travel without the hassle and expense of owning a whole aircraft. Our program offers flexibility, convenience, and access to a fleet of luxurious jets, allowing you to travel in style and comfort.</p>
    <div class="ticks" style="left:656px;top:1061px">
      <span style="left:0;top:0">Flexible Ownership Options</span>
      <span style="left:246px;top:0">Convenient booking process</span>
      <span style="left:0;top:36px">Luxurious fleet of jets</span>
    </div>
    <a class="btn btn-solid sm" style="left:656px;top:1150px">Explore</a>
    <a class="btn btn-line sm" style="left:819px;top:1150px">Sign up</a>
  </section>

  <section class="programs">
    <article class="card" style="left:66px">
      <span class="ring"></span>
      <h3>Flexible ownership options available</h3>
      <p>Choose from a variety of ownership programs and enjoy the freedom to fly on your own terms.</p>
    </article>
    <article class="card" style="left:428px">
      <span class="ring"></span>
      <h3>Convenient jet card programs</h3>
      <p>Access a fleet of private jets with our exclusive jet card programs, offering flexibility and convenience.</p>
    </article>
    <article class="card" style="left:790px">
      <span class="ring"></span>
      <h3>Flexible lease programs</h3>
      <p>Experience the luxury of private jet travel without the commitment with our flexible lease programs.</p>
    </article>
  </section>

  <section class="band">
    <div class="photo band-photo" role="img" aria-label="Jet cabin with facing leather seats and polished wood tables"></div>
    <h2 class="display" style="left:66px;top:1895px;width:520px">Experience luxury travel like never before</h2>
    <p class="lede" style="left:66px;top:2013px;width:600px;color:#fff">Access a fleet of private jets with our exclusive jet card programs, offering</p>
    <a class="btn btn-solid" style="left:66px;top:2059px">Explore</a>
    <a class="btn btn-line" style="left:236px;top:2059px">Learn More</a>
  </section>

  <section class="experience">
    <div class="frame" style="top:2233px"></div>
    <div class="photo side-photo business-photo" role="img" aria-label="Business traveller on a phone call with a laptop in a jet cabin"></div>
    <div class="eyebrow case" style="left:656px;top:2242px">Experience</div>
    <h2 class="display" style="left:656px;top:2270px;width:460px">Unparalleled Luxury and Convenience for Private Aviation</h2>
    <p class="lede" style="left:656px;top:2448px;width:475px">Discover the ultimate in luxury and convenience with SoarVane Our exclusive private aviation solutions provide you with unparalleled access to the world of private jets, ensuring a seamless and extraordinary travel experience. Convenience</p>
    <div class="feature" style="left:656px;top:2562px">
      <h4>Convenience</h4>
      <p>Enjoy hassle-free travel with our flexible scheduling and personalized services.</p>
    </div>
    <div class="feature" style="left:940px;top:2562px;width:200px">
      <h4>Luxury</h4>
      <p>Indulge in the lavish amenities and exquisite interiors of our private jets.</p>
    </div>
    <a class="btn btn-solid sm" style="left:656px;top:2688px">Explore</a>
    <a class="btn btn-line sm" style="left:819px;top:2688px">Sign up</a>
  </section>

  <section class="services">
    <div class="eyebrow" style="left:66px;top:2827px">Luxury</div>
    <h2 class="display" style="left:66px;top:2850px;width:540px">Experience the Ultimate in Private Jet Travel</h2>
    <p class="lede" style="left:681px;top:2873px;width:450px">SoarVane offers a wide range of exclusive services to meet your private jet travel needs. From fractional jet ownership to on-demand charter flights, we provide the highest level of luxury and convenience.</p>
    <article class="service" style="left:66px">
      <span class="ring"></span>
      <h3>On-Demand Charter</h3>
      <p>Choose from a variety of ownership programs and enjoy the freedom to fly on your own terms.</p>
    </article>
    <article class="service" style="left:451px">
      <span class="ring"></span>
      <h3>Worldwide Care Flights</h3>
      <p>Access a fleet of private jets with our exclusive jet card programs, offering flexibility and convenience.</p>
    </article>
    <article class="service" style="left:839px">
      <span class="ring"></span>
      <h3>Fractional jet ownership</h3>
      <p>Experience the luxury of private jet travel without the commitment with our flexible lease programs.</p>
    </article>
  </section>

</div>
</body>
</html>
```